Lumera Ostvik

I need you to design me a business card, with the same logo you did for my company.
It has to include this information.
Thx.
Contact details and other information I suppose it would be better if they were on the back of the card.
Company Name: LumeraOstvik
Commercial Name: Tomás Ibarra Quesada
Company activity: Cosmetics Distribution
Contact email: support@lumeost.com
Contact email: comercial@lumeost.com
Company website: https: //lumeost.com/
Company phone: +376 418 292
Instagram https://www.instagram.com/lumeraostvik/

```html
<!DOCTYPE html>
<html lang="en">
<head>
<meta charset="utf-8">
<title>Lumera Ostvik — Business Card</title>
<link rel="stylesheet" href="https://fonts.googleapis.com/css2?family=Source+Sans+3:wght@400;600&display=swap">
<style>
  :root {
    --stage: #5c5c5c;
    --card-pink: #fcd9e7;
    --card-light: #ffffff;
    --magenta: #cf1597;
    --logo-pink: #ef9fc4;
    --ink-grey: #6a6a6a;
    --brush-dark: #3a2b27;
    --brush-tan: #b59a80;
    --palette-tone: #8d8aa6;
  }
  * { box-sizing: border-box; margin: 0; padding: 0; }
  html, body { width: 1200px; height: 843px; overflow: hidden; }
  body {
    background: var(--stage);
    position: relative;
    font-family: "Source Sans 3", "Myriad Pro", sans-serif;
  }
  .card {
    position: absolute;
    top: 321px;
    width: 362px;
    height: 201px;
    overflow: hidden;
    background: radial-gradient(ellipse 55% 60% at 50% 50%, var(--card-light) 0%, var(--card-pink) 100%);
  }
  .card--front { left: 213px; }
  .card--back { left: 628px; }

  .product-photo { position: absolute; border-radius: 6px; }
  .product-photo--mascara { left: 0; top: 55px; width: 73px; height: 12px; background: linear-gradient(90deg, #222, #555); }
  .product-photo--powder-brush { left: 0; top: 74px; width: 73px; height: 46px; background: linear-gradient(90deg, #2a2a2a, #7a4a36); border-radius: 0 40px 40px 0; }
  .product-photo--palette {
    left: 0; top: 121px; width: 118px; height: 80px; border-radius: 0;
    background: linear-gradient(135deg, #1e1e1e 0%, var(--palette-tone) 45%, #c9a3ad 75%, #9aa6ad 100%);
    clip-path: polygon(0 43px, 37px 0, 118px 61px, 104px 80px, 0 80px);
  }
  .product-photo--fan-brush { left: 246px; top: 0; width: 91px; height: 73px; background: linear-gradient(200deg, #e8e2dc 0%, var(--brush-tan) 60%, #5a4634 100%); border-radius: 0 0 30px 30px; }
  .product-photo--duo-brush { left: 280px; top: 82px; width: 82px; height: 56px; background: linear-gradient(90deg, #f4f4f4 0%, #1f1f1f 55%, #ddd3c6 100%); border-radius: 30px 0 0 30px; }
  .product-photo--blush-brush { left: 287px; top: 144px; width: 58px; height: 57px; background: linear-gradient(140deg, var(--brush-dark) 0%, #3a2b27 45%, #c9a645 75%, #222 100%); border-radius: 30px 10px 10px 10px; }

  .brand {
    position: absolute;
    left: 0; right: 0;
    top: 56px;
    display: flex;
    flex-direction: column;
    align-items: center;
    gap: 3px;
  }
  .brand__mark {
    width: 64px; height: 64px;
    border-radius: 50%;
    background: var(--logo-pink);
  }
  .brand__name {
    font-size: 26px;
    font-weight: 600;
    color: var(--magenta);
    line-height: 1;
    white-space: nowrap;
  }

  .contact {
    position: absolute;
    inset: 0;
    text-align: center;
    color: var(--ink-grey);
  }
  .contact__company { position: absolute; left: 0; right: 0; top: 30px; font-size: 14px; font-weight: 600; color: var(--magenta); line-height: 1.1; }
  .contact__person { position: absolute; left: 0; right: 0; top: 50px; font-size: 11.5px; line-height: 1.1; }
  .contact__role { position: absolute; left: 0; right: 0; top: 64px; font-size: 8px; line-height: 1.1; }
  .contact__line {
    position: absolute; left: 0; right: 0;
    display: flex; justify-content: center; align-items: center; gap: 4px;
    font-size: 11.5px; line-height: 1;
    white-space: nowrap;
  }
  .contact__line svg { width: 11px; height: 11px; stroke: var(--ink-grey); fill: none; stroke-width: 1; flex: none; }
  .contact__line--support { top: 100px; }
  .contact__line--commercial { top: 114px; }
  .contact__line--web { top: 128px; }
  .contact__line--phone { top: 143px; font-size: 12.5px; font-weight: 600; color: var(--magenta); }
  .contact__line--social { top: 159px; }
  .social-dot { width: 9px; height: 9px; border: 1px solid var(--ink-grey); border-radius: 2px; flex: none; }
</style>
</head>
<body>
  <section class="card card--front" aria-label="Business card front">
    <div class="product-photo product-photo--mascara" role="img" aria-label="Photo of a mascara wand"></div>
    <div class="product-photo product-photo--powder-brush" role="img" aria-label="Photo of a brown powder brush"></div>
    <div class="product-photo product-photo--palette" role="img" aria-label="Photo of an eyeshadow palette"></div>
    <div class="product-photo product-photo--fan-brush" role="img" aria-label="Photo of a fan brush"></div>
    <div class="product-photo product-photo--duo-brush" role="img" aria-label="Photo of a duo-fibre stippling brush"></div>
    <div class="product-photo product-photo--blush-brush" role="img" aria-label="Photo of a blush brush with gold ferrule"></div>
    <div class="brand">
      <span class="brand__mark"></span>
      <span class="brand__name">Lumera Ostvik</span>
    </div>
  </section>

  <section class="card card--back" aria-label="Business card back">
    <div class="contact">
      <p class="contact__company">LumeraOstvik</p>
      <p class="contact__person">Tomás Ibarra Quesada</p>
      <p class="contact__role">Cosmetics Distribution</p>
      <p class="contact__line contact__line--support">
        <svg viewBox="0 0 12 12"><rect x="0.5" y="2.5" width="11" height="7"/><path d="M0.5 2.5 6 7 11.5 2.5M0.5 9.5 4.5 5.8M11.5 9.5 7.5 5.8"/></svg>
        support@lumeost.com
      </p>
      <p class="contact__line contact__line--commercial">
        <svg viewBox="0 0 12 12"><rect x="0.5" y="2.5" width="11" height="7"/><path d="M0.5 2.5 6 7 11.5 2.5M0.5 9.5 4.5 5.8M11.5 9.5 7.5 5.8"/></svg>
        comercial@lumeost.com
      </p>
      <p class="contact__line contact__line--web">
        <svg viewBox="0 0 12 12"><circle cx="6" cy="6" r="5.2"/><ellipse cx="6" cy="6" rx="2.3" ry="5.2"/><path d="M0.8 6h10.4M1.6 3.4h8.8M1.6 8.6h8.8"/></svg>
        www.lumeost.com
      </p>
      <p class="contact__line contact__line--phone">+376 418 292</p>
      <p class="contact__line contact__line--social">
        <span class="social-dot"></span>
        www.instagram.com/lumeraostvik
      </p>
    </div>
  </section>
</body>
</html>
```